Urgent - brand new business card for a startup technical advisory and incubation business in Sydney

We need a brand new business card design for BrightForge. We are a startup technical advisory and incubation business based in Sydney Australia. We work with entrepreneurs and innovators to help rapidly and efficiently turn their ideas into reality and to ensure they have the technical platform required for growth.

Our name is partly inspired by our love of lean product development methods and the lean startup movement.

We would like clean, uncluttered designs that feature our two logo colours and communicate a professional but creative, in-touch and entrepreneurial business.

PLEASE SEE MUST HAVE PRIORITIES FOR DRAFT CONTACT INFORMATION AND OTHER DESIRED TEXT ON CARD.
Updates

We have now updated the brief to include draft business card contact information and also some additional desired text to feature on the card design.    Please review the Must Have priorities.

Also final updated source files for the horizontal and vertical versions have now been uploaded and should be used for any designs.

Thanks!

Target Market(s)

Entrepeneurs, innovators, startup investors looking for a strong product development partner

Industry/Entity Type

Business

Requirements
Must have
• Feature our two logo colours
Be a relatively clean, pared back overall design - quite minimalist

Updated source files (AI) for vertical and horizontal layouts attached.

Draft contact information for business card:
Tom Harcourt
Founder & CTO
Phone: +61 427 555123
Email: xxxx@brightforge.example
Callwave: xxxxxharcourt
Chirper: tharcourt

www.brightforge.example

We would also like the overall design to include the phrase "You have great ideas. Let us make them happen." (probably in a reasonably subtle way)

Nice to have
• Inspire me! Double-sided designs are fine with logo, phrase, (URL?) on one side and contact details on other (+ any other design elements)

Logo on business card can be either with lightbulb above the wording as per example here or to the left of the BrightForge wording - both layouts in files provided.
Should not have
• Shouldn't look like a Pendrel Suite business card template :-)

```html
<!DOCTYPE html>
<html lang="en">
<head>
<meta charset="utf-8">
<title>BrightForge Business Card</title>
<link rel="stylesheet" href="https://fonts.googleapis.com/css2?family=Open+Sans:wght@400;600;700;800&display=swap">
<style>
  :root {
    --page: #e9eaec;
    --card: #ffffff;
    --ink: #262a30;
    --brand-blue: #1a9ad6;
    --blue-1: #1591d0;
    --blue-2: #2fa2dc;
    --blue-3: #5ab6e6;
    --blue-4: #86cbef;
    --grey-1: #d6d7d9;
    --grey-2: #e2e3e5;
    --grey-3: #ececee;
  }
  * { box-sizing: border-box; margin: 0; padding: 0; }
  html, body { width: 1200px; height: 1200px; overflow: hidden; }
  body {
    background: var(--page);
    font-family: "Open Sans", Arial, sans-serif;
    color: var(--ink);
    position: relative;
  }
  .card {
    position: absolute;
    left: 250px;
    width: 700px;
    height: 400px;
    background: var(--card);
    overflow: hidden;
    box-shadow: 0 6px 18px rgba(0,0,0,0.12);
  }
  .card--front { top: 140px; }
  .card--back { top: 660px; }
  .card__art { position: absolute; inset: 0; width: 700px; height: 400px; }

  .brand {
    position: absolute;
    display: flex;
    align-items: center;
    gap: 10px;
    color: var(--brand-blue);
    font-weight: 800;
    letter-spacing: -0.5px;
  }
  .brand__dot {
    width: 18px; height: 18px;
    border-radius: 50%;
    background: var(--brand-blue);
  }
  .card--front .brand { top: 100px; left: 0; right: 0; justify-content: center; font-size: 50px; }
  .card--front .brand__dot { width: 24px; height: 24px; }
  .card--back .brand { top: 48px; left: 36px; font-size: 34px; }

  .person {
    position: absolute;
    top: 102px;
    right: 40px;
    text-align: right;
  }
  .person__name {
    font-size: 30px;
    font-weight: 700;
    letter-spacing: -0.5px;
    line-height: 1;
    color: var(--ink);
    padding-bottom: 4px;
  }
  .person__rule {
    position: absolute;
    left: -36px; right: 0; top: 34px;
    height: 2px;
    background: var(--brand-blue);
  }
  .person__rule::before {
    content: "";
    position: absolute;
    left: -4px; top: -3px;
    width: 8px; height: 8px;
    border-radius: 50%;
    background: var(--brand-blue);
  }
  .person__role {
    font-size: 13px;
    margin-top: 6px;
    color: var(--ink);
  }

  .contact {
    position: absolute;
    list-style: none;
  }
  .contact--primary { left: 28px; top: 186px; color: #ffffff; font-size: 15px; }
  .contact--primary li { height: 35px; line-height: 35px; }
  .contact--social { inset: 0; color: var(--ink); font-size: 14px; }
  .contact--social li {
    position: absolute;
    right: 14px;
    height: 40px;
    line-height: 40px;
    white-space: nowrap;
  }
  .contact--social .contact__callwave { top: 290px; }
  .contact--social .contact__chirper { top: 330px; right: 40px; }
</style>
</head>
<body>

  <section class="card card--front" aria-label="Business card front">
    <svg class="card__art" viewBox="0 0 700 400" aria-hidden="true">
      <defs>
        <clipPath id="front-blue">
          <polygon points="240,192 700,192 700,332 330,332"/>
        </clipPath>
        <clipPath id="front-grey">
          <polygon points="0,192 222,192 272,262 0,262"/>
        </clipPath>
      </defs>
      <g clip-path="url(#front-grey)">
        <rect x="0" y="192" width="700" height="35" fill="var(--grey-1)"/>
        <rect x="0" y="227" width="700" height="35" fill="var(--grey-2)"/>
      </g>
      <g clip-path="url(#front-blue)">
        <rect x="0" y="192" width="700" height="35" fill="var(--blue-1)"/>
        <rect x="0" y="227" width="700" height="35" fill="var(--blue-2)"/>
        <rect x="0" y="262" width="700" height="35" fill="var(--blue-3)"/>
        <rect x="0" y="297" width="700" height="35" fill="var(--blue-4)"/>
      </g>
    </svg>
    <div class="brand"><span class="brand__dot"></span>BrightForge</div>
  </section>

  <section class="card card--back" aria-label="Business card back">
    <svg class="card__art" viewBox="0 0 700 400" aria-hidden="true">
      <defs>
        <clipPath id="back-blue">
          <polygon points="0,186 600,186 470,326 0,326"/>
        </clipPath>
        <clipPath id="back-grey">
          <polygon points="581,250 700,250 700,370 469,370"/>
        </clipPath>
      </defs>
      <g clip-path="url(#back-blue)">
        <rect x="0" y="186" width="700" height="35" fill="var(--blue-1)"/>
        <rect x="0" y="221" width="700" height="35" fill="var(--blue-2)"/>
        <rect x="0" y="256" width="700" height="35" fill="var(--blue-3)"/>
        <rect x="0" y="291" width="700" height="35" fill="var(--blue-4)"/>
      </g>
      <g clip-path="url(#back-grey)">
        <rect x="0" y="250" width="700" height="40" fill="var(--grey-1)"/>
        <rect x="0" y="290" width="700" height="40" fill="var(--grey-2)"/>
        <rect x="0" y="330" width="700" height="40" fill="var(--grey-3)"/>
      </g>
    </svg>

    <div class="brand"><span class="brand__dot"></span>BrightForge</div>

    <div class="person">
      <span class="person__rule"></span>
      <p class="person__name">TOM HARCOURT</p>
      <p class="person__role">Founder &amp; CTO</p>
    </div>

    <ul class="contact contact--primary">
      <li>Phone: +61 427 555123</li>
      <li>Email: xxxx@brightforge.example</li>
      <li>Website: www.brightforge.example</li>
    </ul>

    <ul class="contact contact--social">
      <li class="contact__callwave">Callwave: xxxxxharcourt</li>
      <li class="contact__chirper">Chirper: tharcourt</li>
    </ul>
  </section>

</body>
</html>
```